Social Media Graphics - ALL TEXT RK

We are looking for a series of social media graphics for Instagram (standard size 1:1 (1080x1080px) that are ALL TEXT. We want the following quotes below on each graphic; one quote per graphic. AND, In very small letters at the bottom of each graphic, add @RKMarlowLive

The look and feel of these graphics should be complimentary to the color palette attached below; but keep them simple. But the design is up to you; at the end of this document, I provided various samples of all text graphics that I like as examples.

Target Market(s)

women looking to lose weight

Industry/Entity Type

health and wellness

Colors
E54698
E96AAD
F1A4CE
F9D9EA
FCEFF6

Requirements
Must have
• the quotes in the document
Should not have
• no stock photography

```html
<!DOCTYPE html>
<html lang="en">
<head>
<meta charset="utf-8">
<title>RK Social Graphics</title>
<link href="https://fonts.googleapis.com/css2?family=Montserrat:wght@600;700;800&family=Lato:ital,wght@0,700;1,400;1,700&display=swap" rel="stylesheet">
<style>
  :root{
    --stage:#3d3d3d;
    --pink:#e54698;
    --pink-mid:#e96aad;
    --pink-soft:#f1a4ce;
    --pink-pale:#f9d9ea;
    --pink-blush:#fcf0f6;
    --white:#ffffff;
    --ink:#1c1c1c;
    --handle-dark:#7a1a4c;
    --shadow:#d9d9d9;
  }
  *{margin:0;padding:0;box-sizing:border-box}
  html,body{width:1200px;height:1000px;overflow:hidden;background:var(--stage)}
  .canvas{position:relative;width:1200px;height:1000px}
  .post{position:absolute;width:465px;height:465px;overflow:hidden}
  .post--a{left:125px;top:29px;background:var(--white)}
  .post--b{left:611px;top:29px;background:var(--pink-blush)}
  .post--c{left:125px;top:507px;background:var(--pink)}
  .post--d{left:611px;top:507px;background:var(--pink)}
  .post svg.shapes{position:absolute;left:0;top:0}
  .headline{position:absolute;font-family:'Montserrat',sans-serif;font-weight:800;text-transform:uppercase;color:var(--white);text-align:center;line-height:1.12}
  .handle{position:absolute;font-family:'Lato',sans-serif;font-weight:700;font-size:13px;color:var(--white);text-align:center}
  .post--a .headline{left:70px;top:168px;width:325px;font-size:18.5px}
  .post--a .handle{left:70px;top:272px;width:325px}
  .post--b .headline{left:22px;top:110px;width:220px;font-size:15px;line-height:1.35}
  .question{position:absolute;left:130px;top:50px;font-family:'Montserrat',sans-serif;font-weight:800;font-size:150px;color:var(--pink-mid);line-height:1}
  .figure-icon{position:absolute;left:57px;top:160px;width:30px;height:72px;background:var(--ink);border-radius:14px 14px 4px 4px}
  .reply{position:absolute;left:230px;top:238px;width:200px;font-family:'Lato',sans-serif;font-style:italic;font-size:15px;color:var(--ink);text-align:center;line-height:1.4}
  .post--b .handle{left:230px;top:312px;width:200px;color:var(--handle-dark)}
  .quote-mark{position:absolute;width:66px;height:66px;border-radius:50%;background:var(--white);display:flex;align-items:center;justify-content:center;font-family:'Montserrat',sans-serif;font-weight:800;font-style:italic;font-size:44px;color:var(--pink);line-height:1;padding-top:18px}
  .quote-mark--top{left:92px;top:47px}
  .quote-mark--bottom{left:339px;top:350px}
  .body-quote{position:absolute;left:120px;top:157px;width:310px;font-family:'Montserrat',sans-serif;font-weight:600;font-size:16.5px;color:var(--white);text-align:center;line-height:1.3}
  .body-quote .cta{display:block;margin-top:22px}
  .post--c .handle{left:120px;top:272px;width:310px}
  .person-art{position:absolute;left:68px;top:240px;width:100px;height:140px;border-radius:40px 40px 8px 8px;background:linear-gradient(180deg,#f3c9a8 0%,#ffffff 35%,#b9c6d6 100%)}
  .circle-art{position:absolute;left:137px;top:45px;width:192px;height:192px;border-radius:50%;background:radial-gradient(circle,#ffffff 0%,#f9d9ea 55%,#f1a4ce 80%,#e96aad 100%)}
  .post--d .headline{left:40px;top:283px;width:385px;font-size:19.5px;line-height:1.33}
  .post--d .handle{left:40px;top:393px;width:385px}
</style>
</head>
<body>
<main class="canvas">

  <section class="post post--a">
    <svg class="shapes" width="465" height="465" viewBox="0 0 465 465" aria-hidden="true">
      <polygon class="bubble-shadow" points="55,145 55,465 465,465 465,420 260,330 85,100" fill="var(--shadow)" opacity=".7"/>
      <path d="M85,68 h296 a30,30 0 0 1 30,30 v233 a30,30 0 0 1 -30,30 h-90 l-55,60 l-55,-60 h-96 a30,30 0 0 1 -30,-30 v-233 a30,30 0 0 1 30,-30z" fill="var(--pink)"/>
    </svg>
    <h2 class="headline">Wake up tomorrow with a flatter belly- yes, this overnight remedy works like magic!</h2>
    <p class="handle">@RKMarlowLive</p>
  </section>

  <section class="post post--b">
    <svg class="shapes" width="465" height="465" viewBox="0 0 465 465" aria-hidden="true">
      <path d="M33,48 h200 a16,16 0 0 1 16,16 v160 a16,16 0 0 1 -16,16 h-155 l-33,30 v-30 h-12 a16,16 0 0 1 -16,-16 v-160 a16,16 0 0 1 16,-16z" fill="var(--pink)"/>
      <path d="M265,167 h172 a8,8 0 0 1 8,8 v170 a8,8 0 0 1 -8,8 h-56 l-8,55 l-48,-55 h-145 a8,8 0 0 1 -8,-8 v-92" fill="none" stroke="var(--pink)" stroke-width="8" stroke-linejoin="round"/>
    </svg>
    <span class="question" aria-hidden="true">?</span>
    <div class="figure-icon" role="img" aria-label="Small standing person silhouette"></div>
    <h2 class="headline">Struggling with bloating and belly fat?</h2>
    <p class="reply">Try this natural solution tonight, and wake up feeling lighter!</p>
    <p class="handle">@RKMarlowLive</p>
  </section>

  <section class="post post--c">
    <svg class="shapes" width="465" height="465" viewBox="0 0 465 465" aria-hidden="true">
      <path d="M125,80 H52 V340 a42,42 0 0 0 42,42 H372" fill="none" stroke="var(--white)" stroke-width="5"/>
    </svg>
    <div class="quote-mark quote-mark--top" aria-hidden="true">"</div>
    <div class="quote-mark quote-mark--bottom" aria-hidden="true">"</div>
    <p class="body-quote">One supplement, one night; your belly bloat could be gone by morning.<span class="cta">Here's how it works!</span></p>
    <p class="handle">@RKMarlowLive</p>
    <div class="person-art" role="img" aria-label="Illustration of a man holding his bloated belly"></div>
  </section>

  <section class="post post--d">
    <div class="circle-art" role="img" aria-label="Illustration of a woman holding her aching stomach inside a pink circle"></div>
    <h2 class="headline">Finally - a natural solution that flattens your belly and eases stomach bloat</h2>
    <p class="handle">@RKMarlowLive</p>
  </section>

</main>
</body>
</html>
```